TRADE SHOW DISPLAY BANNER Design Project

Looking for a designer to use some photos (that i have taken), edit, cut out, and design a banner for a trade show display that i will be using at an expo.

The approx visible size will be: 295cm wide x 230cm high
(please view display size 1 - for sizes, and display size 2 - for display end product)

Industry/Entity Type

Trade

Requirements
Must have
• - main focus is the steel fence post. will require a picture of the fence with the posts,
photos for this point are ( fence2, fence 3, fence 4, fence 5, fence1 original, fence1)

- the 3 pictures, outlining how the brackets work. on the side
photos for this point are (steel post 1, steel post 2, steel post 3)

Will require 'STEEL FENCE POST' written somewhere on top in large letters. will also require the website written somewhere on the add - 'www.RailvoxUprights.com.au'

Will requite the Dorvell Timber logo somewhere on the bottom corners of the add.
photo of this add is - 'dorvell timber logo'

the exact dimensions of the add can be seen in 'display size1'
the end product of the add will look like 'display size2'

```html
<!DOCTYPE html>
<html lang="en">
<head>
<meta charset="utf-8">
<title>Steel Fence Post – Trade Show Banner</title>
<link rel="stylesheet" href="https://fonts.googleapis.com/css2?family=Roboto:wght@400&family=Roboto+Condensed:wght@400;700;900&family=Open+Sans:wght@400&display=swap">
<style>
  :root {
    --sky: #29a8e0;
    --sky-light: #4fc0ee;
    --sky-pale: #a9d9ef;
    --sky-deep: #1e8fd5;
    --sky-mid: #3aafe6;
    --navy: #13123a;
    --ink: #1f1f5e;
    --white: #ffffff;
  }
  html, body {
    margin: 0;
    padding: 0;
    width: 1200px;
    height: 960px;
    overflow: hidden;
    background: var(--white);
  }
  .banner {
    display: block;
    width: 1200px;
    height: 960px;
  }
  .bg-sky { fill: var(--sky); }
  .band-navy { fill: var(--navy); }
  .stripe-light { fill: var(--sky-light); }
  .stripe-mid { fill: var(--sky-mid); }
  .stripe-deep { fill: var(--sky-deep); }
  .stripe-pale { fill: var(--sky-pale); opacity: .55; }
  .title {
    font-family: "Roboto", Arial, sans-serif;
    font-weight: 400;
    font-size: 162px;
    fill: var(--sky-pale);
  }
  .headline {
    font-family: "Roboto Condensed", "Arial Narrow", sans-serif;
    font-weight: 900;
    font-size: 96px;
    fill: var(--ink);
  }
  .tagline {
    font-family: "Roboto Condensed", "Arial Narrow", sans-serif;
    font-weight: 700;
    font-size: 54px;
    fill: var(--white);
  }
  .website {
    font-family: "Open Sans", Arial, sans-serif;
    font-weight: 400;
    font-size: 48px;
    fill: var(--white);
  }
  .brand-name {
    font-family: "Roboto Condensed", "Arial Narrow", sans-serif;
    font-weight: 900;
    font-size: 66px;
    fill: var(--white);
  }
  .photo-frame {
    stroke: var(--white);
    stroke-width: 3;
  }
</style>
</head>
<body>
<svg class="banner" viewBox="0 0 1200 960" xmlns="http://www.w3.org/2000/svg">
  <defs>
    <linearGradient id="fence-timber" x1="0" y1="0" x2="0" y2="1">
      <stop offset="0" stop-color="#b9a486"/>
      <stop offset="1" stop-color="#8f7658"/>
    </linearGradient>
    <linearGradient id="fence-sunlit" x1="0" y1="0" x2="0" y2="1">
      <stop offset="0" stop-color="#6fa7d6"/>
      <stop offset=".35" stop-color="#d4b58c"/>
      <stop offset="1" stop-color="#a98660"/>
    </linearGradient>
    <linearGradient id="bracket-detail" x1="0" y1="0" x2="0" y2="1">
      <stop offset="0" stop-color="#9a9ea3"/>
      <stop offset=".5" stop-color="#cdb893"/>
      <stop offset="1" stop-color="#8a8e93"/>
    </linearGradient>
    <linearGradient id="fence-corner" x1="0" y1="0" x2="1" y2="0">
      <stop offset="0" stop-color="#8f7a63"/>
      <stop offset="1" stop-color="#bfb5a6"/>
    </linearGradient>
    <filter id="photo-shadow" x="-10%" y="-10%" width="130%" height="130%">
      <feDropShadow dx="6" dy="6" stdDeviation="5" flood-color="#000" flood-opacity=".45"/>
    </filter>
  </defs>

  <!-- base -->
  <rect class="bg-sky" x="0" y="0" width="1200" height="960"/>

  <!-- lower stripe pattern -->
  <g class="stripes">
    <rect class="stripe-deep" x="0" y="483" width="1200" height="32"/>
    <rect class="stripe-light" x="0" y="515" width="620" height="18"/>
    <rect class="stripe-light" x="250" y="550" width="1000" height="30"/>
    <rect class="stripe-pale" x="255" y="553" width="330" height="24"/>
    <rect class="stripe-deep" x="0" y="600" width="1200" height="26"/>
    <rect class="stripe-deep" x="520" y="650" width="680" height="48"/>
    <rect class="stripe-pale" x="2" y="681" width="372" height="18"/>
    <rect class="stripe-deep" x="0" y="700" width="1200" height="28"/>
    <rect class="stripe-light" x="490" y="718" width="620" height="22"/>
    <rect class="stripe-light" x="490" y="746" width="700" height="34"/>
    <rect class="stripe-mid" x="580" y="780" width="620" height="22"/>
    <rect class="stripe-deep" x="580" y="802" width="620" height="30"/>
  </g>

  <!-- title -->
  <text class="title" x="5" y="148" textLength="1180" lengthAdjust="spacingAndGlyphs">STEEL FENCE POST</text>

  <!-- navy photo band -->
  <rect class="band-navy" x="0" y="247" width="1200" height="236"/>

  <!-- product photos -->
  <g class="photos" filter="url(#photo-shadow)">
    <g role="img" aria-label="Photo of a timber paling fence finished against a galvanised steel fence post">
      <rect class="photo-frame" x="66" y="182" width="247" height="353" rx="4" fill="url(#fence-timber)"/>
    </g>
    <g role="img" aria-label="Photo of a long timber fence line held by steel posts beside a house">
      <rect class="photo-frame" x="337" y="182" width="247" height="353" rx="4" fill="url(#fence-sunlit)"/>
    </g>
    <g role="img" aria-label="Close-up photo of a steel bracket bolted to a post and screwed to a timber rail">
      <rect class="photo-frame" x="610" y="182" width="247" height="353" rx="4" fill="url(#bracket-detail)"/>
    </g>
    <g role="img" aria-label="Photo of a fence corner showing rails fixed into the steel post channel">
      <rect class="photo-frame" x="883" y="182" width="249" height="353" rx="4" fill="url(#fence-corner)"/>
    </g>
  </g>

  <!-- headline -->
  <text class="headline" x="66" y="642" textLength="1070" lengthAdjust="spacingAndGlyphs">SLIM, LIGHTWEIGHT &amp; DURABLE</text>
  <text class="tagline" x="1137" y="708" text-anchor="end">The Timber Alternative</text>

  <!-- footer band -->
  <rect class="band-navy" x="0" y="832" width="1200" height="128"/>
  <text class="website" x="71" y="899" textLength="636" lengthAdjust="spacingAndGlyphs">www.RailvoxUprights.com.au</text>

  <!-- brand -->
  <g class="brand">
    <text class="brand-name" x="1127" y="860" text-anchor="end">Dorvell Timber</text>
  </g>
</svg>
</body>
</html>
```